Coral drift hour Banner promoting freedom and adventure working from laptop

I need 3 different banners in 4 different sizes
I am an online business working from home on my laptop. I am in the motivational program and internet marketing industry and would like some banners that reflect healthy, fun and financially free lifestyle.
I have a Chatterly page title of UpWithSun and a website called Coraldrifthour.com
I have uploaded some photos but am unsure what may be required for the banners.
I am on the Gold Coast Australia but will be advertising in America, UK, Canada etc.

Target Market(s)

Adventure and Health fitness

Colors

Designer to choose colors to be used in the design.

Requirements
Must have
• Promotion of a living a financially free life through the ability of working from home via your own online business.
• Fun fit healthy freedom and adventure associated with someone living their dream life from working from home away from the 9 to 5 hustle and bussle.
Nice to have
• beaches, mountains and working from a Zentra slate air.
• Showing fun and adventure from someone living this lifestyle.

```html
<!DOCTYPE html>
<html lang="en">
<head>
<meta charset="utf-8">
<title>Coral drift hour – Work From Home Banner</title>
<link rel="stylesheet" href="https://fonts.googleapis.com/css2?family=Open+Sans:wght@300;400;600;800&display=swap">
<style>
  :root {
    --navy: #0b3563;
    --magenta: #a3178e;
    --white: #ffffff;
    --sky-top: #2f7fcf;
    --sky-mid: #6fb0e6;
    --sea: #3d8fc4;
    --sand: #a9cfe6;
    --desk: #8fb9d8;
    --flag-blue: #1d3a8f;
    --flag-red: #d7263d;
  }
  * { margin: 0; padding: 0; box-sizing: border-box; }
  html, body {
    width: 1200px;
    height: 1200px;
    overflow: hidden;
    background: var(--navy);
  }
  .banner {
    position: relative;
    width: 1200px;
    height: 1200px;
    overflow: hidden;
    font-family: "Open Sans", Arial, sans-serif;
    color: var(--white);
  }
  .banner__photo {
    position: absolute;
    inset: 0;
    background:
      linear-gradient(180deg,
        var(--sky-top) 0%,
        var(--sky-mid) 38%,
        var(--sea) 56%,
        var(--sand) 68%,
        var(--desk) 80%,
        #b8d3e6 100%);
  }
  .banner__shapes {
    position: absolute;
    inset: 0;
    width: 1200px;
    height: 1200px;
  }
  .banner__flag {
    position: absolute;
    left: 52px;
    top: 46px;
    width: 106px;
    height: 72px;
  }
  .headline {
    position: absolute;
    left: 0;
    right: 0;
    text-align: center;
    line-height: 1;
    white-space: nowrap;
  }
  .headline--main {
    top: 474px;
    font-size: 112px;
    font-weight: 800;
    letter-spacing: -1px;
  }
  .headline__accent { color: var(--magenta); }
  .headline--sub {
    top: 650px;
    left: 40px;
    font-size: 70px;
    font-weight: 600;
  }
  .headline--devices {
    top: 722px;
    font-size: 112px;
    font-weight: 300;
    letter-spacing: -1px;
  }
  .tagline {
    position: absolute;
    right: 56px;
    top: 1000px;
    text-align: right;
    font-size: 38px;
    font-weight: 400;
    line-height: 1.12;
    letter-spacing: 0.5px;
    text-transform: uppercase;
  }
  .website {
    position: absolute;
    right: 56px;
    top: 1132px;
    font-size: 18px;
    font-weight: 400;
    letter-spacing: 11px;
    text-transform: uppercase;
  }
</style>
</head>
<body>
  <div class="banner">
    <div class="banner__photo" role="img" aria-label="Photo of three friends jumping joyfully on a sunny beach, with a laptop and tablet on a desk in the foreground, tinted blue"></div>

    <svg class="banner__shapes" viewBox="0 0 1200 1200" aria-hidden="true">
      <path class="shape-top-accent" fill="var(--magenta)"
            d="M0 215 C300 190 700 120 920 0 H1010 C770 175 360 228 0 245 Z"/>
      <path class="shape-top-band" fill="var(--navy)"
            d="M0 0 H920 C700 120 300 190 0 215 Z"/>
      <path class="shape-bottom-accent" fill="var(--magenta)"
            d="M190 1200 C490 985 800 838 1200 826 V850 C800 862 500 1005 215 1200 Z"/>
      <path class="shape-bottom-band" fill="var(--navy)"
            d="M215 1200 C500 1005 800 862 1200 850 V1200 Z"/>
    </svg>

    <svg class="banner__flag" viewBox="0 0 106 72" role="img" aria-label="Australian flag">
      <rect width="106" height="72" fill="var(--flag-blue)"/>
      <g class="flag-union">
        <path d="M0 0 L53 36 M53 0 L0 36" stroke="var(--white)" stroke-width="7"/>
        <path d="M0 0 L53 36 M53 0 L0 36" stroke="var(--flag-red)" stroke-width="2.5"/>
        <path d="M26.5 0 V36 M0 18 H53" stroke="var(--white)" stroke-width="11"/>
        <path d="M26.5 0 V36 M0 18 H53" stroke="var(--flag-red)" stroke-width="6"/>
      </g>
      <g class="flag-stars" fill="var(--white)">
        <circle cx="26.5" cy="55" r="5"/>
        <circle cx="80" cy="15" r="3"/>
        <circle cx="68" cy="34" r="3"/>
        <circle cx="93" cy="30" r="3"/>
        <circle cx="80" cy="60" r="3.2"/>
        <circle cx="86" cy="42" r="1.8"/>
      </g>
    </svg>

    <h1 class="headline headline--main">WORK FROM <span class="headline__accent">HOME</span></h1>
    <p class="headline headline--sub">with your</p>
    <p class="headline headline--devices">LAPTOP AND PHONE</p>

    <p class="tagline">Create the lifestyle<br>you always wanted</p>
    <p class="website">www.coraldrifthour.com</p>
  </div>
</body>
</html>
```